Cruise Booking Website

Cruise search and booking website

This project is a redesign of a cruise booking website we did a few years ago.

The current website is located here: http://voyage.pixelmarsh.com/en/

It's not fully functional but gives you ad idea how miserable the old design was.

All the information about cruises, cruise lines, destinations, ports and shore excursions will be similar to http://www.sailorbay.com/
Actual search pages (form, results, single result, sailing and cabin selection, ship info, booking) will have EXACTLY the same info as sailorbay.com

We like the style of http://harborvoyagehub.com, it's quite modern, good spacing, not overloaded with information. So you can use it as an example of what we like, not what we want as a final result for us. Please, don't copy it. The result should not be possible to resemble the harborvoyagehub.com, because our site has to be unique. This is important!
If you submit a design that clearly reminds another cruise site it will be rejected!

Also the mockup provided is just to give you the basic structure and show what information has to be present on the page. It doesn't mean the layout has to be the same as a mockup. The layout is up to the designer.

I've updated the mockup to be more generic so it doesn't confuse you:
https://www.filecrate.net/s/k7q2mz9pw4tnb3x/Home%20page.png

When you're adding social sharing icons like chatterbox/peeplet you have to use chinese ones instead:
https://www.filecrate.net/s/h3rt8wyd6jcl0fe/chinese-social-icons.png
Originals: http://shrtlk.example/qRmT

We'll start with home page first and after it's approved inner pages can be designed.

I know the cost of the project doesn't look high, but the task is straight forward and doesn't require to be very original, it's better to follow existing design and layout patterns that proved to work well.
That's why I encourage you to choose a template to build the design on top of one of https://themequarry.net/ themes if it will save the design work, will be easier and faster for you. So it will be more like a customization than a new design from scratch.

Mockups, site map and logo files:
- https://www.filecrate.net/sh/50xb7vq1ndtpkez/RmwuHp8Zq3

Website tree:
- https://papers.quillnet.example/document/d/8vTrXk2MqLpZ4wNsB7yHcE1oUjFgD9aR_QbVtnWm/edit?usp=sharing
Updates

So far a lot of designs are just copying http://www.harborvoyagehub.com/ - we don't like it!

We like the style of harborvoyagehub.com, it's quite modern, good spacing, not overloaded with information. So you can use it as an example of what we like, not what we want as a final result for us. Please, don't copy it. The result should not be possible to resemble the harborvoyagehub.com, because our site has to be unique. This is important!

Target Market(s)

Chinese travellers

Industry/Entity Type

Build

Requirements
Must have
• * White, blue and red
* Large spacing, not too much information cramped into a small space like sailorbay.com or the current website
* More "hidden" info in popups, tabs and so on, so not to many things are visible at the same time
* Compatible with lumen framekit styling (for easier coding):
- http://lumenkit.example.io/framework/index.html
- http://skinvault.net/
* Feel free to propose to build the design on top of one of https://themequarry.net/ themes if it will save the design work, will be easier and faster for you

```html
<!DOCTYPE html>
<html lang="en">
<head>
<meta charset="utf-8">
<title>Bluewake – Cruise Booking</title>
<link href="https://fonts.googleapis.com/css2?family=Arimo:wght@400;700&family=Days+One&display=swap" rel="stylesheet">
<style>
:root{
  --red:#a10a0a;
  --red-dark:#7d0606;
  --blue:#2366a3;
  --blue-bright:#1f8fc9;
  --blue-head:#1e86c4;
  --sky-top:#2a63b8;
  --sky-bottom:#b8d7ef;
  --pale:#e6f2fb;
  --pale-2:#c6e3f4;
  --white:#ffffff;
  --grey:#8a8a8a;
  --text:#444;
}
*{margin:0;padding:0;box-sizing:border-box}
html,body{width:1200px;height:1200px;overflow:hidden;background:var(--white)}
body{font-family:"Arimo",Arial,sans-serif;color:var(--text)}
.canvas{position:relative;width:1200px;height:1200px;overflow:hidden}
.abs{position:absolute}

/* top bar */
.topbar{left:0;top:0;width:1200px;height:24px;background:var(--red)}
.top-search{left:667px;top:6px;width:83px;height:13px;border-radius:7px;background:var(--white);font-size:6px;color:#bbb;padding:3px 0 0 12px}
.top-search svg{position:absolute;right:5px;top:2px}
.top-link{top:8px;font-size:8px;color:var(--white)}
.lang{left:851px;top:5px;display:flex;align-items:center;gap:4px;font-size:7px;color:var(--white)}

/* header */
.brand{left:312px;top:62px;display:flex;align-items:center;gap:12px}
.brand-mark{width:58px;height:58px;border-radius:50%;background:var(--blue-head)}
.brand-name{font-family:"Days One",sans-serif;font-size:38px;color:var(--blue);line-height:1}
.brand-url{font-family:"Days One",sans-serif;font-size:10px;color:var(--blue);margin-top:6px;letter-spacing:.5px}
.phone-box{left:644px;top:56px;width:173px;height:32px;border-radius:0 0 16px 16px;background:var(--white);box-shadow:0 3px 4px rgba(0,0,0,.18);display:flex;align-items:center;gap:14px;padding-left:10px}
.phone-box span{font-size:20px;color:var(--red)}
.hours{left:830px;top:61px;font-size:7px;line-height:9px;color:var(--red)}
.head-social{left:826px;top:95px;display:flex;gap:10px}
.dot{width:14px;height:14px;border-radius:50%;background:var(--blue-bright)}

/* navigation */
.nav{left:0;top:157px;width:1200px;height:40px;background:var(--blue)}
.nav ul{position:absolute;left:318px;width:568px;top:13px;display:flex;justify-content:space-between;list-style:none}
.nav li{font-size:9px;color:var(--white)}
.nav li.active{position:relative}
.nav li.active::after{content:"";position:absolute;left:22px;top:20px;border:5px solid transparent;border-bottom-color:var(--white)}
.subnav{left:318px;top:208px;display:flex;gap:14px;list-style:none}
.subnav li{font-size:9px;color:var(--blue)}

/* hero */
.hero{left:0;top:228px;width:1200px;height:330px;background:linear-gradient(180deg,var(--sky-top) 0%,#4f8fd4 45%,var(--sky-bottom) 80%,#e9eef2 100%)}
.hero-rule{left:0;top:558px;width:1200px;height:4px;background:var(--blue-bright)}
.finder{left:317px;top:259px;width:296px;height:235px;background:var(--red);border-radius:6px 6px 6px 6px;box-shadow:0 2px 5px rgba(0,0,0,.3)}
.finder-label{left:25px;font-size:8px;font-weight:700;color:var(--white)}
.select{left:141px;width:119px;height:24px;border-radius:12px;background:var(--white);font-size:7px;color:#888;padding:7px 0 0 20px}
.select::after{content:"";position:absolute;right:10px;top:9px;border:5px solid transparent;border-top:7px solid #777}
.adv{left:103px;top:210px;font-size:8px;color:var(--white)}
.btn-search{left:183px;top:198px;width:77px;height:25px;border-radius:5px;background:var(--blue-bright);color:var(--white);font-size:11px;font-weight:700;text-align:center;padding-top:6px;box-shadow:0 2px 2px rgba(0,0,0,.35)}

/* content */
.content-band{left:0;top:562px;width:1200px;height:342px;background:linear-gradient(180deg,var(--pale) 0%,var(--pale-2) 100%)}
.tabs{left:312px;top:589px;display:flex;height:41px}
.tab{background:var(--blue-bright);color:var(--white);font-size:8px;padding:16px 9px 0;height:41px}
.tab.current{background:var(--white);color:var(--blue);border-radius:5px 0 0 0;padding:16px 12px 0}
.tab:last-child{border-radius:0 5px 0 0}
.panel{left:312px;top:630px;width:576px;height:260px;background:var(--white);border-radius:0 5px 5px 5px}
.photo-frame{left:24px;top:26px;width:190px;height:120px;border:1px solid #bbb;padding:3px;background:var(--white)}
.photo{width:100%;height:100%}
.panel h2{position:absolute;left:238px;top:25px;font-family:"Days One",sans-serif;font-weight:400;font-size:18px;color:var(--blue-head)}
.copy{font-size:6.6px;line-height:8.6px;color:#555}
.copy-side{left:238px;top:54px;width:166px}
.copy-wide{left:24px;top:166px;width:380px}
.news{left:413px;top:26px;width:139px;height:219px;border:1px solid #bbb}
.news-photo{position:absolute;left:15px;top:11px;width:108px;height:84px}
.news h3{position:absolute;left:0;width:100%;top:106px;text-align:center;font-size:8px;color:var(--blue);font-weight:700}
.news p{position:absolute;left:15px;top:127px;width:110px;font-size:6.6px;line-height:8.6px;color:#555}
.email{position:absolute;left:16px;top:155px;width:108px;height:21px;border:1px solid #aaa;border-radius:10px;font-size:7px;color:#666;padding:6px 0 0 12px}
.btn-sub{position:absolute;left:59px;top:187px;width:66px;height:23px;border-radius:5px;background:var(--red);color:var(--white);font-size:10px;font-weight:700;text-align:center;padding-top:6px;box-shadow:0 2px 2px rgba(0,0,0,.35)}

/* partners */
.partners-title{left:312px;top:925px;font-family:"Days One",sans-serif;font-size:14px;color:var(--blue-head)}
.arrow{top:958px;width:19px;height:19px;border:1px solid var(--blue-bright);border-radius:50%}
.arrow::after{content:"";position:absolute;top:5px;border:4px solid transparent}
.arrow.prev::after{left:3px;border-right:5px solid var(--blue-bright)}
.arrow.next::after{left:7px;border-left:5px solid var(--blue-bright)}
.badge{top:962px;width:66px;height:14px;border-radius:3px;background:#c9c9c9}

/* footer */
.footer{left:0;top:996px;width:1200px;height:142px;background:linear-gradient(180deg,#8fc6e5 0%,#cfe7f4 100%)}
.foot-col h4{font-family:"Days One",sans-serif;font-weight:400;font-size:14px;color:var(--red);margin-bottom:12px}
.foot-col ul{list-style:none}
.foot-col li{font-size:8px;line-height:10px;color:var(--blue)}
.about-row{display:flex;gap:10px}
.about-mark{display:flex;flex-direction:column;align-items:center;gap:4px}
.about-mark .circle{width:40px;height:40px;border-radius:50%;background:var(--blue-head)}
.about-mark span{font-size:8px;font-weight:700;color:var(--blue)}
.about-row p{width:76px;font-size:6.8px;line-height:8.6px;color:var(--blue)}
.contact-line{display:flex;gap:10px;align-items:flex-start;font-size:6.8px;line-height:8.6px;color:var(--blue);margin-bottom:9px}
.contact-line svg{flex:none}

.bottombar{left:0;top:1138px;width:1200px;height:62px;background:var(--blue)}
.copyright{left:312px;top:1161px;font-size:6.5px;color:var(--white)}
.bottom-lang{left:312px;top:1175px;display:flex;gap:4px;align-items:center;font-size:6px;color:var(--white)}
.foot-social{left:815px;top:1162px;display:flex;gap:12px}
.foot-social .dot{width:16px;height:16px;background:var(--white)}
</style>
</head>
<body>
<div class="canvas">

  <!-- top bar -->
  <div class="abs topbar"></div>
  <div class="abs top-search">Search
    <svg width="8" height="8" viewBox="0 0 8 8"><circle cx="3" cy="3" r="2.2" fill="none" stroke="#555" stroke-width="1"/><line x1="4.6" y1="4.6" x2="7.5" y2="7.5" stroke="#555" stroke-width="1.2"/></svg>
  </div>
  <div class="abs top-link" style="left:774px">Login</div>
  <div class="abs top-link" style="left:812px">Sign up</div>
  <div class="abs lang">
    <svg width="13" height="13" viewBox="0 0 13 13"><circle cx="6.5" cy="6.5" r="5.8" fill="none" stroke="#fff"/><ellipse cx="6.5" cy="6.5" rx="2.5" ry="5.8" fill="none" stroke="#fff"/><line x1="0.7" y1="6.5" x2="12.3" y2="6.5" stroke="#fff"/></svg>
    <span>中文</span><span style="margin-left:6px">▾</span>
  </div>

  <!-- header -->
  <div class="abs brand">
    <div class="brand-mark"></div>
    <div>
      <div class="brand-name">Bluewake</div>
      <div class="brand-url">www.bluewake.example</div>
    </div>
  </div>
  <div class="abs phone-box">
    <svg width="20" height="20" viewBox="0 0 24 24"><path d="M6.6 10.8a15 15 0 0 0 6.6 6.6l2.2-2.2a1 1 0 0 1 1-.25 11.4 11.4 0 0 0 3.6.57 1 1 0 0 1 1 1V20a1 1 0 0 1-1 1A17 17 0 0 1 3 4a1 1 0 0 1 1-1h3.5a1 1 0 0 1 1 1c0 1.25.2 2.45.57 3.6a1 1 0 0 1-.25 1z" fill="#1f7fbf"/></svg>
    <span>4008 512 630</span>
  </div>
  <div class="abs hours">Book online or call<br>9:00AM- 18:00PM<br>Monday to Friday</div>
  <div class="abs head-social"><div class="dot"></div><div class="dot"></div><div class="dot"></div></div>

  <!-- navigation -->
  <nav class="abs nav">
    <ul>
      <li>Home</li><li class="active">Destinations ˅</li><li>Cruise Lines</li><li>Cruise Info</li><li>Deals</li><li>Online Booking</li><li>Contact us</li><li>Blog</li><li>Search</li>
    </ul>
  </nav>
  <ul class="abs subnav">
    <li>China</li><li>Indonesia</li><li>Thailand</li><li>Round Asia</li><li>China</li><li>Indonesia</li><li>Thailand</li><li>Round Asia</li>
  </ul>

  <!-- hero -->
  <div class="abs hero" role="img" aria-label="Photo of a white cruise ship deck under a blue sky framed by palm leaves"></div>
  <div class="abs hero-rule"></div>
  <form class="abs finder">
    <div class="abs finder-label" style="top:24px">Choose your destination</div>
    <div class="abs select" style="top:17px">Asia</div>
    <div class="abs finder-label" style="top:69px">Choose Dates</div>
    <div class="abs select" style="top:62px">July 2013</div>
    <div class="abs finder-label" style="top:116px">Select Lenght</div>
    <div class="abs select" style="top:109px">Any length</div>
    <div class="abs finder-label" style="top:163px">Select Cruise</div>
    <div class="abs select" style="top:156px">Any Cruise</div>
    <div class="abs adv">Advanced Search</div>
    <div class="abs btn-search">search</div>
  </form>

  <!-- content -->
  <div class="abs content-band"></div>
  <div class="abs tabs">
    <div class="tab current">Book with us</div>
    <div class="tab">Deals</div>
    <div class="tab">Packages</div>
    <div class="tab">News</div>
    <div class="tab">First time cruiser?</div>
  </div>
  <section class="abs panel">
    <div class="abs photo-frame">
      <div class="photo" role="img" aria-label="Photo of a cruise ship at sea seen past a traveller in a straw hat on a turquoise beach" style="background:linear-gradient(180deg,#3b84d6 0%,#7fc3ef 45%,#1fb6d6 60%,#35c8d2 100%)"></div>
    </div>
    <h2>Book with us</h2>
    <p class="abs copy copy-side">Chocolate jelly candy cupcake apple pie chocolate cheesecake. Chocolate bar chocolate bar topping caramels tootsie roll. Brownie wafer sweet pudding powder gummi bears macaroon tootsie roll.<br>Chocolate jelly candy cupcake apple pie chocolate cheesecake. Chocolate bar chocolate bar topping caramels tootsie roll. Brownie wafer sweet pudding powder gummi bears macaroon tootsie roll.<br>Chocolate jelly candy cupcake apple pie chocolate cheesecake. Chocolate bar chocolate bar topping caramels tootsie roll. Brownie wafer sweet pudding powder gummi bears macaroon tootsie roll.</p>
    <p class="abs copy copy-wide">Chocolate jelly candy cupcake apple pie chocolate cheesecake. Chocolate bar chocolate bar topping caramels tootsie roll. Brownie wafer sweet pudding powder gummi bears macaroon tootsie roll.<br>Chocolate jelly candy cupcake apple pie chocolate cheesecake. Chocolate bar chocolate bar topping caramels tootsie roll. Brownie wafer sweet pudding powder gummi bears macaroon tootsie roll.<br>Chocolate jelly candy cupcake apple pie chocolate cheesecake. Chocolate bar chocolate bar topping caramels tootsie roll. Brownie wafer sweet pudding powder gummi bears macaroon tootsie roll.</p>
    <aside class="abs news">
      <div class="news-photo" role="img" aria-label="Photo of a lit cruise ship on calm water at dusk" style="background:linear-gradient(180deg,#1c2c5a 0%,#4a5d8f 45%,#c98a6a 62%,#243a5e 100%)"></div>
      <h3>Cruise deals Newsletter</h3>
      <p>Chocolate jelly candy cupcake apple pie chocolate cheesecake.</p>
      <div class="email">e - mail</div>
      <div class="btn-sub">subscribe</div>
    </aside>
  </section>

  <!-- partners -->
  <h3 class="abs partners-title">Our Reliable Partners</h3>
  <div class="abs arrow prev" style="left:293px"></div>
  <div class="abs badge" style="left:332px"></div>
  <div class="abs badge" style="left:430px"></div>
  <div class="abs badge" style="left:523px"></div>
  <div class="abs badge" style="left:619px"></div>
  <div class="abs badge" style="left:717px"></div>
  <div class="abs badge" style="left:807px"></div>
  <div class="abs arrow next" style="left:888px"></div>

  <!-- footer -->
  <footer class="abs footer"></footer>
  <div class="abs foot-col" style="left:312px;top:1023px">
    <h4>Useful Pages</h4>
    <ul><li>About us</li><li>Contact us</li><li>Terms of Service</li><li>Paymnet Info</li></ul>
  </div>
  <div class="abs foot-col" style="left:458px;top:1023px">
    <h4>Cruise info</h4>
    <ul><li>Cruise news</li><li>Visa</li><li>Honeymoon Cruises</li><li>First time on a cruise</li></ul>
  </div>
  <div class="abs foot-col" style="left:598px;top:1023px">
    <h4>About bluewake.example</h4>
    <div class="about-row">
      <div class="about-mark"><div class="circle"></div><span>Bluewake</span></div>
      <p>Chocolate jelly candy cupcake apple pie chocolate cheesecake. Chocolate bar chocolate bar topping caramels tootsie roll. Brownie wafer sweet</p>
    </div>
  </div>
  <div class="abs foot-col" style="left:793px;top:1023px">
    <h4>Contact us</h4>
    <div class="contact-line">
      <svg width="11" height="14" viewBox="0 0 11 14"><path d="M5.5 0A5.5 5.5 0 0 0 0 5.5C0 9.6 5.5 14 5.5 14S11 9.6 11 5.5A5.5 5.5 0 0 0 5.5 0z" fill="#2366a3"/><circle cx="5.5" cy="5.3" r="2" fill="#cfe7f4"/></svg>
      <span>Chocolate jelly 32, 12035<br><b>Indonesia</b></span>
    </div>
    <div class="contact-line">
      <svg width="12" height="12" viewBox="0 0 24 24"><path d="M6.6 10.8a15 15 0 0 0 6.6 6.6l2.2-2.2a1 1 0 0 1 1-.25 11.4 11.4 0 0 0 3.6.57 1 1 0 0 1 1 1V20a1 1 0 0 1-1 1A17 17 0 0 1 3 4a1 1 0 0 1 1-1h3.5a1 1 0 0 1 1 1c0 1.25.2 2.45.57 3.6a1 1 0 0 1-.25 1z" fill="#2366a3"/></svg>
      <span>4008 512 630</span>
    </div>
    <div class="contact-line">
      <svg width="14" height="10" viewBox="0 0 14 10"><rect x=".5" y=".5" width="13" height="9" fill="none" stroke="#2366a3"/><path d="M.5 .5 7 6 13.5 .5" fill="none" stroke="#2366a3"/></svg>
      <span>hello@bluewake.example</span>
    </div>
  </div>

  <div class="abs bottombar"></div>
  <div class="abs copyright">© 2013 bluewake.example. All rights reserved</div>
  <div class="abs bottom-lang">
    <svg width="11" height="11" viewBox="0 0 13 13"><circle cx="6.5" cy="6.5" r="5.8" fill="none" stroke="#fff"/><ellipse cx="6.5" cy="6.5" rx="2.5" ry="5.8" fill="none" stroke="#fff"/><line x1="0.7" y1="6.5" x2="12.3" y2="6.5" stroke="#fff"/></svg>
    <span>中文</span>
  </div>
  <div class="abs foot-social"><div class="dot"></div><div class="dot"></div><div class="dot"></div></div>

</div>
</body>
</html>
```